Vex Pim ORA Need a custom graphic

I need to have the attached chart re-designed in a hand colored pencil format. The heading needs to be changed to "The most effective methods for hiring sales people". Do not include the background logo in the sample file.

Place the attached Vex Pim ORA logo next to the most effective methods (91%)

```html
<!DOCTYPE html>
<html lang="en">
<head>
<meta charset="utf-8">
<title>The Most Effective Methods for Hiring Sales People</title>
<link rel="stylesheet" href="https://fonts.googleapis.com/css2?family=Montserrat:wght@400;600;700;800&family=Oswald:wght@500&display=swap">
<style>
  :root {
    --stage: #9c9c9c;
    --paper: #fbfcfd;
    --blue: #1593d3;
    --blue-light: #3aaee6;
    --navy: #1f2f6b;
    --ink: #1b1b1f;
    --grid: #c9e4f4;
    --white: #ffffff;
  }
  html, body {
    margin: 0;
    width: 1096px;
    height: 1200px;
    overflow: hidden;
    background: var(--stage);
  }
  .infographic {
    position: absolute;
    left: 20px;
    top: 272px;
    width: 1056px;
    height: 655px;
    box-shadow: 0 12px 30px rgba(0,0,0,.35);
  }
  .infographic svg { display: block; width: 100%; height: 100%; }
  .brand-name { font: 800 46px "Montserrat", sans-serif; fill: var(--navy); }
  .brand-tagline { font: 600 12px "Montserrat", sans-serif; fill: var(--navy); letter-spacing: 1px; }
  .title { font: 800 35px "Montserrat", sans-serif; fill: var(--white); letter-spacing: .5px; }
  .axis-value { font: 700 13px "Montserrat", sans-serif; fill: var(--ink); }
  .axis-title { font: 800 16px "Montserrat", sans-serif; fill: var(--blue); }
  .axis-title .strong { fill: var(--navy); }
  .point-label { font: 800 15px "Montserrat", sans-serif; fill: var(--ink); }
  .point-label tspan { font-size: 9px; }
  .badge-text { font: 800 16px "Montserrat", sans-serif; fill: var(--white); }
  .badge-text tspan { font-size: 9px; }
  .method-text { font: 700 10.5px "Montserrat", sans-serif; fill: var(--white); }
  .footer-title { font: 500 40px "Oswald", sans-serif; fill: var(--white); letter-spacing: -1px; }
  .footer-title .accent { fill: var(--blue-light); }
</style>
</head>
<body>
<main class="infographic">
<svg viewBox="0 0 1255 778" xmlns="http://www.w3.org/2000/svg">
  <rect class="sheet" width="1255" height="778" fill="var(--paper)"/>
  <path class="corner-tab" d="M0 0H52V90Q52 115 27 115H0Z" fill="var(--blue)"/>

  <g class="brand">
    <text class="brand-name" x="100" y="100">VEX PIM ORA</text>
    <text class="brand-tagline" x="102" y="124">YOUR A.I. SALES RECRUITER</text>
  </g>

  <g class="header-banner">
    <path d="M560 0H1255V145H565Q560 125 558 95L525 70L558 40Q560 20 560 0Z" fill="var(--blue)"/>
    <path d="M565 128Q700 150 860 138Q1050 126 1255 145V150H565Z" fill="var(--blue)"/>
    <text class="title" x="600" y="70">THE MOST EFFECTIVE METHODS</text>
    <text class="title" x="600" y="108">FOR HIRING SALES PEOPLE</text>
  </g>

  <g class="grid" stroke="var(--grid)" stroke-width="1">
    <path d="M195 170V692M273 170V692M351 170V692M429 170V692M507 170V692M585 170V692M663 170V692M741 170V692M819 170V692M897 170V692M973 170V692"/>
    <path d="M117 170H973M117 222H973M117 274H973M117 326H973M117 378H973M117 430H973M117 482H973M117 534H973M117 587H973M117 639H973"/>
  </g>

  <g class="axes" stroke="var(--ink)" stroke-width="3.5" fill="none" stroke-linecap="round" stroke-linejoin="round">
    <path d="M118 692L115 178"/>
    <path d="M103 196L115 174L131 194"/>
    <path d="M118 692L990 690"/>
    <path d="M960 672L992 690L958 714"/>
  </g>

  <g class="y-values">
    <text class="axis-value" x="72" y="222">0.90</text>
    <text class="axis-value" x="72" y="274">0.80</text>
    <text class="axis-value" x="72" y="326">0.70</text>
    <text class="axis-value" x="72" y="378">0.60</text>
    <text class="axis-value" x="72" y="431">0.50</text>
    <text class="axis-value" x="72" y="483">0.40</text>
    <text class="axis-value" x="72" y="535">0.30</text>
    <text class="axis-value" x="72" y="588">0.20</text>
    <text class="axis-value" x="72" y="640">0.10</text>
    <text class="axis-value" x="72" y="692">0.00</text>
  </g>

  <g class="y-title">
    <path d="M34 200V312M40 200V312M34 548V692M40 548V692" stroke="var(--blue)" stroke-width="2"/>
    <text class="axis-title" transform="translate(43 535) rotate(-90)">PREDICTIVE <tspan class="strong">VALIDITY</tspan></text>
  </g>

  <g class="leaders" stroke="var(--ink)" stroke-width="1.2" stroke-dasharray="2 2">
    <path d="M175 615V640M235 595V572M323 588V612M398 588V564M485 571V596M561 569V544M637 517V540M715 420V396M779 390V414M867 311V290M963 213V238"/>
  </g>

  <polyline class="data-line" points="175,615 235,595 323,588 398,588 485,571 561,569 637,517 715,420 779,390 867,311 963,213" fill="none" stroke="var(--ink)" stroke-width="3" stroke-linejoin="round"/>
  <g class="data-points" stroke="var(--ink)" stroke-width="2">
    <circle cx="175" cy="615" r="8" fill="var(--blue)"/>
    <circle cx="235" cy="595" r="8" fill="var(--navy)"/>
    <circle cx="323" cy="588" r="8" fill="var(--blue)"/>
    <circle cx="398" cy="588" r="8" fill="var(--navy)"/>
    <circle cx="485" cy="571" r="8" fill="var(--blue)"/>
    <circle cx="561" cy="569" r="8" fill="var(--navy)"/>
    <circle cx="637" cy="517" r="8" fill="var(--blue)"/>
    <circle cx="715" cy="420" r="8" fill="var(--navy)"/>
    <circle cx="779" cy="390" r="8" fill="var(--blue)"/>
    <circle cx="867" cy="311" r="8" fill="var(--navy)"/>
    <circle cx="963" cy="213" r="8" fill="var(--blue)"/>
  </g>

  <g class="point-labels" text-anchor="middle">
    <text class="point-label" x="174" y="662">13<tspan dy="-6">%</tspan></text>
    <text class="point-label" x="238" y="561">18<tspan dy="-6">%</tspan></text>
    <text class="point-label" x="323" y="636">20<tspan dy="-6">%</tspan></text>
    <text class="point-label" x="402" y="553">20<tspan dy="-6">%</tspan></text>
    <text class="point-label" x="488" y="618">23<tspan dy="-6">%</tspan></text>
    <text class="point-label" x="560" y="533">23<tspan dy="-6">%</tspan></text>
    <text class="point-label" x="638" y="562">33<tspan dy="-6">%</tspan></text>
    <text class="point-label" x="715" y="386">51<tspan dy="-6">%</tspan></text>
    <text class="point-label" x="779" y="437">57<tspan dy="-6">%</tspan></text>
    <text class="point-label" x="867" y="279">71<tspan dy="-6">%</tspan></text>
    <text class="point-label" x="957" y="260">91<tspan dy="-6">%</tspan></text>
  </g>

  <g class="legend">
    <defs>
      <g id="badge">
        <rect x="0" y="-19" width="40" height="38" rx="7" fill="var(--navy)"/>
        <rect x="-3" y="-21" width="40" height="38" rx="7" fill="var(--blue)"/>
      </g>
    </defs>

    <g transform="translate(1010 188)"><use href="#badge"/><text class="badge-text" x="1" y="5">91<tspan dy="-6">%</tspan></text>
      <rect x="45" y="-25" width="167" height="52" rx="10" fill="none" stroke="var(--blue)" stroke-width="1.5"/>
      <path d="M50 -20H200Q210 -20 210 -10V14Q200 20 180 16Q160 24 150 22H58Q50 22 50 14Z" fill="var(--navy)"/>
      <text class="method-text" x="68" y="-7">SALES-SPECIFIC</text><text class="method-text" x="68" y="4">MULTI-MEASUREMENT</text><text class="method-text" x="68" y="15">ASSESSMENT</text></g>

    <g transform="translate(1010 244)"><use href="#badge"/><text class="badge-text" x="1" y="5">71<tspan dy="-6">%</tspan></text>
      <rect x="45" y="-20" width="167" height="42" rx="10" fill="none" stroke="var(--blue)" stroke-width="1.5"/>
      <path d="M50 -15H200Q210 -15 210 -5V10Q200 16 180 12Q160 19 150 17H58Q50 17 50 9Z" fill="var(--navy)"/>
      <text class="method-text" x="68" y="-2">MULTI-MEASUREMENT</text><text class="method-text" x="68" y="9">ASSESSMENT,</text></g>

    <g transform="translate(1010 300)"><use href="#badge"/><text class="badge-text" x="1" y="5">57<tspan dy="-6">%</tspan></text>
      <rect x="45" y="-25" width="167" height="52" rx="10" fill="none" stroke="var(--blue)" stroke-width="1.5"/>
      <path d="M50 -20H200Q210 -20 210 -10V14Q200 20 180 16Q160 24 150 22H58Q50 22 50 14Z" fill="var(--navy)"/>
      <text class="method-text" x="63" y="-7">HIGHLY</text><text class="method-text" x="63" y="4">STRUCTURED INTERVIEW</text><text class="method-text" x="63" y="15">WITH SCORECARD</text></g>

    <g transform="translate(1010 354)"><use href="#badge"/><text class="badge-text" x="1" y="5">51<tspan dy="-6">%</tspan></text>
      <rect x="45" y="-20" width="167" height="42" rx="10" fill="none" stroke="var(--blue)" stroke-width="1.5"/>
      <path d="M50 -15H200Q210 -15 210 -5V10Q200 16 180 12Q160 19 150 17H58Q50 17 50 9Z" fill="var(--navy)"/>
      <text class="method-text" x="66" y="-2">GENERAL MENTAL</text><text class="method-text" x="66" y="9">ABILITY</text></g>

    <g transform="translate(1010 403)"><use href="#badge"/><text class="badge-text" x="1" y="5">33<tspan dy="-6">%</tspan></text>
      <rect x="45" y="-17" width="167" height="36" rx="10" fill="none" stroke="var(--blue)" stroke-width="1.5"/>
      <path d="M50 -12H200Q210 -12 210 -3V8Q200 13 180 10Q160 16 150 14H58Q50 14 50 7Z" fill="var(--navy)"/>
      <text class="method-text" x="65" y="4">REFERENCE CHECK</text></g>

    <g transform="translate(1010 447)"><use href="#badge"/><text class="badge-text" x="1" y="5">23<tspan dy="-6">%</tspan></text>
      <rect x="45" y="-20" width="167" height="42" rx="10" fill="none" stroke="var(--blue)" stroke-width="1.5"/>
      <path d="M50 -15H200Q210 -15 210 -5V10Q200 16 180 12Q160 19 150 17H58Q50 17 50 9Z" fill="var(--navy)"/>
      <text class="method-text" x="70" y="-2">BEHAVIOR/</text><text class="method-text" x="70" y="9">PERSONALITY TEST,</text></g>

    <g transform="translate(1010 494)"><use href="#badge"/><text class="badge-text" x="1" y="5">23<tspan dy="-6">%</tspan></text>
      <rect x="45" y="-17" width="167" height="36" rx="10" fill="none" stroke="var(--blue)" stroke-width="1.5"/>
      <path d="M50 -12H200Q210 -12 210 -3V8Q200 13 180 10Q160 16 150 14H58Q50 14 50 7Z" fill="var(--navy)"/>
      <text class="method-text" x="70" y="4">RESUME</text></g>

    <g transform="translate(1010 540)"><use href="#badge"/><text class="badge-text" x="1" y="5">20<tspan dy="-6">%</tspan></text>
      <rect x="45" y="-17" width="167" height="36" rx="10" fill="none" stroke="var(--blue)" stroke-width="1.5"/>
      <path d="M50 -12H200Q210 -12 210 -3V8Q200 13 180 10Q160 16 150 14H58Q50 14 50 7Z" fill="var(--navy)"/>
      <text class="method-text" x="70" y="4">SKILLS TEST</text></g>

    <g transform="translate(1010 585)"><use href="#badge"/><text class="badge-text" x="1" y="5">20<tspan dy="-6">%</tspan></text>
      <rect x="45" y="-20" width="167" height="42" rx="10" fill="none" stroke="var(--blue)" stroke-width="1.5"/>
      <path d="M50 -15H200Q210 -15 210 -5V10Q200 16 180 12Q160 19 150 17H58Q50 17 50 9Z" fill="var(--navy)"/>
      <text class="method-text" x="70" y="-2">TRADITIONAL</text><text class="method-text" x="70" y="9">INTERVIEW</text></g>

    <g transform="translate(1010 634)"><use href="#badge"/><text class="badge-text" x="1" y="5">18<tspan dy="-6">%</tspan></text>
      <rect x="45" y="-20" width="167" height="42" rx="10" fill="none" stroke="var(--blue)" stroke-width="1.5"/>
      <path d="M50 -15H200Q210 -15 210 -5V10Q200 16 180 12Q160 19 150 17H58Q50 17 50 9Z" fill="var(--navy)"/>
      <text class="method-text" x="70" y="-2">EMOTIONAL</text><text class="method-text" x="70" y="9">INTELLIGENCE</text></g>

    <g transform="translate(1010 682)"><use href="#badge"/><text class="badge-text" x="1" y="5">13<tspan dy="-6">%</tspan></text>
      <rect x="45" y="-17" width="167" height="36" rx="10" fill="none" stroke="var(--blue)" stroke-width="1.5"/>
      <path d="M50 -12H200Q210 -12 210 -3V8Q200 13 180 10Q160 16 150 14H58Q50 14 50 7Z" fill="var(--navy)"/>
      <text class="method-text" x="70" y="4">CULTURE TEST</text></g>
  </g>

  <g class="footer">
    <path d="M0 755Q150 745 300 752Q420 758 470 740V778H0Z" fill="var(--blue)"/>
    <path d="M790 740Q900 752 1050 742Q1160 735 1255 738V778H790Z" fill="var(--blue)"/>
    <path d="M442 778L465 718Q470 704 485 704H760Q775 704 780 718L812 778Z" fill="var(--navy)"/>
    <text class="footer-title" x="625" y="760" text-anchor="middle">HIRING <tspan class="accent">METODE</tspan></text>
  </g>
</svg>
</main>
</body>
</html>
```